Women's Online Clothing Boutique Needs Business Cards

I already have a logo that I would like to use. Some of the things that interest me is black business cards, foil embossed logo, glossy embossed logo, leopard print, no yellow font, rounded edges. I even like just a large logo on the front side with all of my information on the back side.

Contact Information for Business Card

https://silverheron.shopvenlo.com/
https://www.pagelink.net/thesilverheronboutique/
https://www.picfeed.net/thesilverheronboutique/
silverheronboutique@mailora.net

Requirements
Must have
• My Logo
Nice to have
• Leopard Print
Should not have
• No Yellow Font

```html
<!DOCTYPE html>
<html lang="en">
<head>
<meta charset="utf-8">
<title>The Silver Heron Boutique — Business Card</title>
<link rel="stylesheet" href="https://fonts.googleapis.com/css2?family=Jost:wght@300;400&display=swap">
<style>
  :root {
    --stage: #161616;
    --card-black: #050505;
    --silver: #b9b9bb;
    --silver-dim: #8a8a8c;
    --text-light: #e6e6e6;
    --gold-light: #e9c98a;
    --gold-mid: #d2a75a;
    --gold-deep: #b58a3e;
    --icon-gold: #c9a24f;
  }
  * { margin: 0; padding: 0; box-sizing: border-box; }
  html, body {
    width: 1200px;
    height: 900px;
    overflow: hidden;
    background: var(--stage);
    font-family: "Jost", sans-serif;
  }
  .stage {
    width: 1200px;
    height: 900px;
    display: flex;
    flex-direction: column;
    align-items: center;
    justify-content: center;
    gap: 48px;
  }
  .card {
    width: 630px;
    height: 360px;
    border-radius: 28px;
    background: var(--card-black);
    overflow: hidden;
    position: relative;
    box-shadow: 0 18px 40px rgba(0,0,0,.55);
  }

  /* Front: brand name */
  .card-front {
    display: flex;
    align-items: center;
    justify-content: center;
  }
  .brand {
    display: flex;
    align-items: center;
    gap: 18px;
  }
  .brand-mark {
    width: 22px;
    height: 22px;
    border-radius: 50%;
    background: var(--silver);
  }
  .brand-name {
    font-weight: 300;
    font-size: 44px;
    letter-spacing: .5px;
    color: var(--silver);
    line-height: 1;
  }

  /* Back: pattern bands and contact details */
  .pattern-band {
    position: absolute;
    left: 0;
    right: 0;
    background: linear-gradient(100deg, var(--gold-light) 0%, var(--gold-mid) 50%, var(--gold-deep) 100%);
  }
  .pattern-band--top { top: 0; height: 92px; }
  .pattern-band--bottom { bottom: 0; height: 104px; }
  .contact-list {
    position: absolute;
    top: 120px;
    left: 150px;
    list-style: none;
    display: flex;
    flex-direction: column;
    gap: 10px;
  }
  .contact-item {
    display: flex;
    align-items: center;
    gap: 12px;
    font-weight: 300;
    font-size: 22px;
    color: var(--text-light);
    line-height: 1.1;
  }
  .contact-icons { display: flex; gap: 4px; width: 38px; justify-content: flex-end; }
  .contact-icon { width: 17px; height: 17px; flex: none; }
</style>
</head>
<body>
<main class="stage">

  <section class="card card-front" aria-label="Business card front">
    <div class="brand">
      <span class="brand-mark"></span>
      <span class="brand-name">The Silver Heron Boutique</span>
    </div>
  </section>

  <section class="card card-back" aria-label="Business card back">
    <div class="pattern-band pattern-band--top" role="img" aria-label="Gold and black leopard print band"></div>

    <ul class="contact-list">
      <li class="contact-item">
        <span class="contact-icons">
          <svg class="contact-icon" viewBox="0 0 20 20" aria-hidden="true">
            <circle cx="10" cy="10" r="10" fill="var(--icon-gold)"/>
            <rect x="5" y="6.5" width="10" height="7" fill="none" stroke="#111" stroke-width="1.2"/>
            <path d="M5 6.5 L10 10.5 L15 6.5" fill="none" stroke="#111" stroke-width="1.2"/>
          </svg>
        </span>
        silverheronboutique@mailora.net
      </li>
      <li class="contact-item">
        <span class="contact-icons">
          <svg class="contact-icon" viewBox="0 0 20 20" aria-hidden="true">
            <circle cx="10" cy="10" r="10" fill="var(--icon-gold)"/>
            <circle cx="10" cy="10" r="5" fill="none" stroke="#111" stroke-width="1.1"/>
            <ellipse cx="10" cy="10" rx="2.2" ry="5" fill="none" stroke="#111" stroke-width="1.1"/>
            <line x1="5" y1="10" x2="15" y2="10" stroke="#111" stroke-width="1.1"/>
          </svg>
        </span>
        silverheron.shopvenlo.com
      </li>
      <li class="contact-item">
        <span class="contact-icons">
          <svg class="contact-icon" viewBox="0 0 20 20" aria-hidden="true">
            <circle cx="10" cy="10" r="10" fill="var(--icon-gold)"/>
          </svg>
          <svg class="contact-icon" viewBox="0 0 20 20" aria-hidden="true">
            <circle cx="10" cy="10" r="10" fill="var(--icon-gold)"/>
          </svg>
        </span>
        /thesilverheronboutique
      </li>
    </ul>

    <div class="pattern-band pattern-band--bottom" role="img" aria-label="Gold and black leopard print band"></div>
  </section>

</main>
</body>
</html>
```